Stationery Design Project

see attached logo and business card layout, envelopes, letterhead, proposal, and invoice stationery needs to all flow.

Industry/Entity Type

Business

```html
<!DOCTYPE html>
<html lang="en">
<head>
<meta charset="utf-8">
<title>Business Card – Account Manager</title>
<link rel="stylesheet" href="https://fonts.googleapis.com/css2?family=Arimo:wght@400&display=swap">
<style>
  :root {
    --sun-top: #fdd733;
    --sun-mid: #fbe58a;
    --cream-bottom: #fffaec;
    --ink-dark: #2b2b2b;
    --panel-black: #080a09;
    --contact-grey: #6b6b6b;
  }
  html, body {
    margin: 0;
    padding: 0;
    width: 1200px;
    height: 684px;
    overflow: hidden;
  }
  .business-card {
    position: relative;
    width: 1200px;
    height: 684px;
    background: linear-gradient(to bottom, var(--sun-top) 0%, var(--sun-mid) 40%, var(--cream-bottom) 100%);
    font-family: "Arimo", Arial, sans-serif;
  }
  .card-art {
    position: absolute;
    inset: 0;
    width: 1200px;
    height: 684px;
    display: block;
  }
  .contact-panel { fill: var(--panel-black); }
  .office-address {
    fill: var(--ink-dark);
    font-size: 39px;
    font-family: "Arimo", Arial, sans-serif;
  }
  .contact-line {
    fill: var(--contact-grey);
    font-size: 35px;
    font-family: "Arimo", Arial, sans-serif;
  }
</style>
</head>
<body>
  <main class="business-card">
    <svg class="card-art" viewBox="0 0 1200 684" xmlns="http://www.w3.org/2000/svg">
      <rect class="contact-panel" x="162" y="321" width="1038" height="262"/>
      <text class="office-address" x="206" y="319" textLength="954" lengthAdjust="spacingAndGlyphs">4800 HARBOR DR SUITE 310 LINDALE, CA 90417</text>
      <text class="contact-line" x="446" y="409" text-anchor="middle">Tel : 555,210,4400</text>
      <text class="contact-line" x="912" y="409" text-anchor="middle">Fax : 555,210,4402</text>
      <text class="contact-line" x="390" y="459" text-anchor="middle">Cell : 555,210,7788</text>
      <text class="contact-line" x="928" y="459" text-anchor="middle">Email : mdelvane@lindale.co</text>
      <text class="contact-line" x="681" y="538" text-anchor="middle">Marco Delvane : Account Manager</text>
    </svg>
  </main>
</body>
</html>
```